Stationary Design for Norvath Digital

We are after a full stationary back business cards, letterheads, compliment slip, invoice template, delivery note and anything else we could use within the stationary pack.

We would also like an email footer creating.

Our company details to be included on all stationary:

Registered Name: Norvath Limited
Company Registration Number: 20473915
Website: www.norvathdigital.example
email: info@norvathdigital.example
Phone: 01632 960 417
Address: 48 Tamsin Lane Harrowfield Westmereshire United Kingdom HF3 9QX

```html
<!DOCTYPE html>
<html lang="en">
<head>
<meta charset="utf-8">
<title>Norvath Digital – Business Card</title>
<link rel="stylesheet" href="https://fonts.googleapis.com/css2?family=Play:wght@400;700&display=swap">
<style>
  :root {
    --navy: #0d2c5e;
    --navy-deep: #0a2a5a;
    --paper: #f1f1f3;
    --ink: #4a4a4f;
    --rule: #6d6d72;
    --backdrop: #9a9a9a;
    --light: #e6e8ee;
  }
  * { margin: 0; padding: 0; box-sizing: border-box; }
  html, body {
    width: 1105px; height: 1200px; overflow: hidden;
    background: var(--backdrop);
    font-family: "Play", sans-serif;
  }
  .card {
    position: absolute;
    left: 182px;
    width: 746px;
    height: 425px;
  }
  .card--front { top: 119px; background: var(--paper); color: var(--ink); }
  .card--back { top: 637px; background: var(--navy-deep); color: var(--light); }

  .brand {
    position: absolute;
    font-weight: 700;
    letter-spacing: 1px;
    white-space: nowrap;
    display: flex;
    align-items: center;
  }
  .card--front .brand { right: 37px; top: 80px; font-size: 42px; color: var(--navy); }
  .card--back .brand { left: 0; right: 0; top: 200px; justify-content: center; font-size: 52px; color: var(--light); }

  .holder { position: absolute; left: 33px; right: 36px; top: 192px; }
  .holder__name { font-size: 26px; font-weight: 700; color: var(--navy); letter-spacing: 0.5px; }
  .holder__role {
    display: flex; align-items: center; gap: 8px;
    font-size: 19px; color: var(--ink); margin-top: 4px;
  }
  .holder__role::after { content: ""; flex: 1; height: 1px; background: var(--rule); }

  .company { position: absolute; left: 33px; top: 268px; font-size: 19px; line-height: 26px; font-style: normal; }
  .company__name { font-weight: 700; color: #2f2f34; }

  .contact { position: absolute; right: 34px; top: 312px; list-style: none; text-align: right; }
  .contact li {
    display: flex; justify-content: flex-end; align-items: center; gap: 14px;
    font-size: 19px; line-height: 29px;
  }
  .contact svg { width: 18px; height: 18px; fill: var(--navy); flex: none; }

  .card--back .site {
    position: absolute; left: 0; right: 0; top: 360px;
    text-align: center; font-size: 20px; letter-spacing: 5px; color: var(--light);
  }
</style>
</head>
<body>
  <section class="card card--front">
    <div class="brand"><span class="brand__name">NORVATH DIGITAL</span></div>

    <div class="holder">
      <div class="holder__name">DANIEL REEVE</div>
      <div class="holder__role">CEO/FOUNDER</div>
    </div>

    <address class="company">
      <div class="company__name">Norvath Limited</div>
      <div>48 Tamsin Lane Harrowfield</div>
      <div>Westmereshire</div>
      <div>United Kingdom HF3 9QX</div>
      <div>Reg. No: 20473915</div>
    </address>

    <ul class="contact">
      <li>01632 960 417
        <svg viewBox="0 0 24 24" aria-hidden="true"><path d="M6.6 10.8a15.1 15.1 0 0 0 6.6 6.6l2.2-2.2a1 1 0 0 1 1-.25 11.4 11.4 0 0 0 3.6.57 1 1 0 0 1 1 1V20a1 1 0 0 1-1 1A17 17 0 0 1 3 4a1 1 0 0 1 1-1h3.5a1 1 0 0 1 1 1c0 1.25.2 2.45.57 3.57a1 1 0 0 1-.25 1z"/></svg>
      </li>
      <li>info@norvathdigital.example
        <svg viewBox="0 0 24 24" aria-hidden="true"><path d="M2 5h20v14H2z M3.5 6.5 12 12.5l8.5-6z" fill-rule="evenodd"/></svg>
      </li>
      <li>www.norvathdigital.example
        <svg viewBox="0 0 24 24" aria-hidden="true"><path d="M12 2a10 10 0 1 0 0 20 10 10 0 0 0 0-20zm-1 17.9A8 8 0 0 1 4.1 10.6L9 15.5v1a2 2 0 0 0 2 2zm6.9-2.5A2 2 0 0 0 16 16h-1v-3a1 1 0 0 0-1-1H8v-2h2a1 1 0 0 0 1-1V7h2a2 2 0 0 0 2-2v-.4a8 8 0 0 1 2.9 12.8z"/></svg>
      </li>
    </ul>
  </section>

  <section class="card card--back">
    <div class="brand"><span class="brand__name">NORVATH DIGITAL</span></div>
    <div class="site">WWW.NORVATHDIGITAL.EXAMPLE</div>
  </section>
</body>
</html>
```